Business Card Design

We need a business card design for a new company called Velmar Joinery. We make, design and install all joinery.
We want a classy business card which is not to busy, we want a double sided card with just the logo on one side and all the required information on the other. We are a partnership so would like cards with both names and numbers. We would like to see a design which blends in with our logo and really makes it pop.

Reason: I would like my logo displayed on the business card please.

Industry/Entity Type

Business

Contact Information for Business Card

Name- Dean Velmar Phone Number- 047318562
Name- Luke Velmar Phone Number- 0418265931 E-mail- velmarjoinery@examplemail.net
License Number- 583920k Company Name- Velmar Joinery ABN-47 508 293 614

Colors
0456a4
ffffff

```html
<!DOCTYPE html>
<html lang="en">
<head>
<meta charset="utf-8">
<title>Velmar Joinery – Business Card</title>
<link rel="stylesheet" href="https://fonts.googleapis.com/css2?family=Source+Sans+3:wght@400;600&family=Montserrat:wght@600&display=swap">
<style>
  :root {
    --navy: #283891;
    --brand-blue: #0456a4;
    --orange: #f26a2a;
    --yellow: #ffde17;
    --white: #ffffff;
    --ink: #1a1a1a;
    --page: #f2f2f2;
  }
  * { margin: 0; padding: 0; box-sizing: border-box; }
  html, body {
    width: 1200px;
    height: 1075px;
    overflow: hidden;
    background: var(--page);
  }
  .canvas {
    position: relative;
    width: 1200px;
    height: 1075px;
  }
  .card {
    position: absolute;
    left: 170px;
    width: 860px;
    height: 490px;
    background: var(--white);
    border: 2px solid var(--ink);
    border-radius: 40px 40px 0 0;
    overflow: hidden;
    font-family: "Source Sans 3", sans-serif;
  }
  .card--info { top: 35px; }
  .card--logo { top: 550px; }

  /* Info side */
  .info__band {
    position: absolute;
    left: 0; right: 0;
    top: 165px; bottom: 0;
    background: var(--navy);
  }
  .info__abn-strip {
    position: absolute;
    left: 0; right: 0;
    top: 400px;
    height: 50px;
    background: var(--yellow);
    display: flex;
    align-items: center;
    justify-content: center;
    font-family: "Montserrat", sans-serif;
    font-weight: 600;
    font-size: 30px;
    letter-spacing: 3px;
    color: var(--navy);
  }
  .partner {
    position: absolute;
    color: var(--navy);
    line-height: 1;
  }
  .partner__name { font-size: 44px; font-weight: 400; }
  .partner__phone { font-size: 28px; margin-top: 4px; padding-left: 40px; }
  .partner--left { left: 70px; top: 70px; }
  .partner--right { right: 70px; top: 22px; text-align: left; }
  .company {
    position: absolute;
    left: 0; right: 0;
    top: 205px;
    text-align: center;
    color: var(--orange);
  }
  .company__name { font-size: 44px; font-weight: 400; }
  .company__details {
    margin-top: 22px;
    font-size: 27px;
    line-height: 1.2;
  }

  /* Logo side */
  .logo-side__band {
    position: absolute;
    left: 0; right: 0;
    bottom: 0;
    height: 175px;
    background: var(--navy);
  }
  .wordmark {
    position: absolute;
    left: 0; right: 0;
    top: 120px;
    display: flex;
    align-items: center;
    justify-content: center;
    gap: 26px;
  }
  .wordmark__square {
    width: 78px;
    height: 78px;
    background: var(--brand-blue);
  }
  .wordmark__name {
    font-family: "Source Sans 3", sans-serif;
    font-weight: 600;
    font-size: 82px;
    color: var(--brand-blue);
    letter-spacing: 1px;
  }
</style>
</head>
<body>
<main class="canvas">
  <section class="card card--info" aria-label="Business card, contact side">
    <div class="info__band"></div>
    <div class="partner partner--left">
      <p class="partner__name">Dean Velmar</p>
      <p class="partner__phone">047318562</p>
    </div>
    <div class="partner partner--right">
      <p class="partner__name">Luke Velmar</p>
      <p class="partner__phone">0418265931</p>
    </div>
    <div class="company">
      <p class="company__name">Velmar Joinery</p>
      <p class="company__details">E-mail- velmarjoinery@examplemail.net<br>License Number- 583920k</p>
    </div>
    <div class="info__abn-strip">ABN-47 508 293 614</div>
  </section>

  <section class="card card--logo" aria-label="Business card, logo side">
    <div class="wordmark">
      <span class="wordmark__square"></span>
      <span class="wordmark__name">Velmar Joinery</span>
    </div>
    <div class="logo-side__band"></div>
  </section>
</main>
</body>
</html>
```